Pilates trainer needs new website

Summary: I need a new, meaningful website in a 1-page format, but one that can be expanded if necessary. I teach in various studios and in the future also in companies. Therefore, the website should convey growth, joy, uniqueness, workout and a bit of luxury.
The website should be inviting.
Layout:
Introduction what I offer
A bit about me
Option to upload price list and timetable in PDF format
Studio address where I teach
The color scheme should be petrol, gold, and colors that match. Not too dark, please.
My current website www.pilates-wendmarau.de, new domain is pilates-corvanel.com (I have already purchased it)
Logo file attached
I have attached a few suggestions but I am also happy to be surprised.

Target Market(s)

Pilates private and small groups,

Industry/Entity Type

Pilates teacher freelancer

Coding

Coded - Design and coding required

Number of Pages Required

1 page

Requirements
Must have
• Welcoming appearance, about me, pictures, offers, colors from the logo but don't get do dark, more fresh and a bit luxurious
Should not have
• Not too wild and going crazy with colors

```html
<!DOCTYPE html>
<html lang="en">
<head>
<meta charset="utf-8">
<title>Mara Lindqvist – Pilates Studio Trainer</title>
<link rel="stylesheet" href="https://fonts.googleapis.com/css2?family=Poppins:wght@400;500;600&family=Cinzel:wght@400;500&family=Playfair+Display:wght@700&display=swap">
<style>
:root{
  --teal:#0aa89a;
  --teal-light:#66ebdf;
  --gold:#dda10f;
  --ink:#2a2a2a;
  --muted:#666;
  --soft:#f2f2f2;
  --photo-light:#e6e6e6;
  --photo-mid:#b9b9b9;
  --white:#fff;
}
*{box-sizing:border-box;margin:0;padding:0}
html,body{width:1200px;height:3928px;overflow:hidden}
body{position:relative;font-family:"Poppins",sans-serif;color:var(--ink);background:var(--white)}
.btn{position:absolute;display:flex;align-items:center;justify-content:center;background:var(--gold);color:var(--white);border-radius:26px;font-size:18px;font-weight:500;text-transform:uppercase}
.display{font-family:"Cinzel",serif;font-weight:400;letter-spacing:2px}

/* header */
.site-header{position:absolute;left:0;top:0;width:1200px;height:120px}
.brand{position:absolute;left:96px;top:36px;font-size:20px;font-weight:500;color:var(--gold);display:flex;align-items:center;gap:8px}
.brand-dot{width:14px;height:14px;border-radius:50%;background:var(--gold)}
.main-nav{position:absolute;left:268px;top:38px;display:flex;gap:26px;font-size:18px;color:#555}
.main-nav .active{color:var(--gold);text-decoration:underline;text-underline-offset:4px}
.lang{position:absolute;left:862px;top:38px;font-size:17px;font-weight:600;color:#555;display:flex;gap:20px;align-items:center}
.login{left:1017px;top:24px;width:99px;height:51px;text-transform:none;font-size:19px}

/* hero */
.hero{position:absolute;left:0;top:120px;width:1200px;height:464px;background:linear-gradient(90deg,var(--teal) 0%,var(--teal) 45%,var(--teal-light) 100%)}
.hero-title{position:absolute;left:84px;top:68px;color:var(--white);font-size:33px;line-height:34px}
.hero-text{position:absolute;left:84px;top:152px;width:480px;color:var(--white);font-size:20px;line-height:30px}
.hero .btn{left:84px;top:345px;width:341px;height:51px}
.hero-art{position:absolute;left:622px;top:93px}

/* about */
.about-art{position:absolute;left:84px;top:668px}
.about-title{position:absolute;left:538px;top:664px;font-size:36px;line-height:34px}
.about-text{position:absolute;left:538px;top:783px;width:570px;font-size:20px;line-height:30px;color:var(--muted)}
.about .btn{left:538px;top:974px;width:162px;height:51px}

/* services */
.section-title{position:absolute;left:0;width:1200px;text-align:center;font-size:36px}
.section-sub{position:absolute;left:0;width:1200px;text-align:center;font-size:20px;color:var(--muted)}
.service{position:absolute;top:1336px;width:300px;text-align:center}
.service svg{display:block;margin:0 auto}
.service h3{font-size:24px;font-weight:500;margin-top:42px}
.service p{font-size:20px;line-height:30px;color:var(--muted);margin:12px auto 0;width:240px}

/* subscribe */
.subscribe{position:absolute;left:0;top:1781px;width:1200px;height:331px;background:linear-gradient(90deg,#b0164f 0%,#c73e66 22%,#d9566a 50%,#d35a66 72%,#8f5a32 74%,#a06a3a 100%)}
.subscribe .display{position:absolute;top:82px;width:1200px;text-align:center;color:var(--white);font-size:33px}
.subscribe p{position:absolute;top:133px;width:1200px;text-align:center;color:var(--white);font-size:20px}
.subscribe .btn{left:500px;top:195px;width:198px;height:51px}

/* testimonials */
.testimonial{position:absolute;top:2318px;width:500px;height:350px}
.testimonial-photo{position:absolute;left:0;top:0;width:500px;height:350px;border-radius:18px;background:linear-gradient(180deg,var(--photo-light) 0%,var(--photo-mid) 100%)}
.testimonial-body{position:absolute;left:0;top:222px;width:438px;height:204px;background:var(--white);border-radius:0 26px 0 0;padding:30px 16px}
.author{display:flex;align-items:center;gap:14px;font-size:21px;font-weight:600}
.avatar{width:50px;height:50px;border-radius:50%;background:#c9b59a}
.quote{font-size:18px;line-height:27px;color:var(--muted);margin-top:16px}
.time{font-size:20px;font-weight:500;margin-top:14px}

/* contact */
.contact-panel{position:absolute;left:84px;top:2905px;width:1032px;height:467px;background:linear-gradient(90deg,var(--teal) 40%,var(--teal) 70%,var(--teal-light) 100%)}
.contact-photo{position:absolute;left:84px;top:2851px;width:454px;height:572px;clip-path:polygon(0 4%,6% 0,100% 49%,100% 52%,6% 100%,0 96%);background:linear-gradient(135deg,#d9a57c 0%,#a86a48 50%,#5c3a2c 100%)}
.contact-title{position:absolute;left:579px;top:2952px;font-family:"Playfair Display",serif;font-size:32px;color:var(--white)}
.field{position:absolute;height:49px;border-radius:6px;background:rgba(255,255,255,.22);color:var(--white);font-size:22px;padding:8px 18px}
.contact .btn{left:569px;top:3291px;width:161px;height:50px;text-transform:none;font-size:19px;font-weight:600}

/* footer */
.site-footer{position:absolute;left:0;top:3532px;width:1200px;height:396px;background:linear-gradient(90deg,var(--teal) 0%,var(--teal) 70%,var(--teal-light) 100%);color:var(--white)}
.footer-brand{position:absolute;left:110px;top:98px;font-size:22px;font-weight:500}
.social{position:absolute;top:164px;width:40px;height:40px;border-radius:50%;background:var(--white)}
.footer-col{position:absolute;top:64px}
.footer-col h4{font-size:21px;font-weight:600;margin-bottom:14px}
.footer-col a{display:block;color:var(--white);text-decoration:none;font-size:18px;line-height:39px}
.footer-rule{position:absolute;left:84px;top:327px;width:1032px;height:1px;background:rgba(255,255,255,.8)}
.legal{position:absolute;top:346px;width:1200px;text-align:center;font-size:20px;font-weight:500}
</style>
</head>
<body>

<header class="site-header">
  <div class="brand"><span class="brand-dot"></span>Corvanel</div>
  <nav class="main-nav">
    <span class="active">Home</span><span>About</span><span>News</span><span>FAQ</span><span>Support</span><span>Contact us</span>
  </nav>
  <div class="lang">ENG
    <svg width="14" height="10" viewBox="0 0 14 10"><path d="M2 2l5 5 5-5" fill="none" stroke="#dda10f" stroke-width="2"/></svg>
  </div>
  <a class="btn login">Login</a>
</header>

<section class="hero">
  <h1 class="hero-title display">Mara Lindqvist<br>Pilates Studio Trainer</h1>
  <p class="hero-text">The first prerequisite for being able to carry out our many different daily tasks with pleasure and joy is physical fitness, a consistently well-trained body and full possession of our mental faculties.</p>
  <a class="btn">Request an appointment now</a>
  <svg class="hero-art" width="499" height="277" viewBox="408 140 327 181" role="img" aria-label="Three triangular photos of women doing Pilates outdoors and on mats">
    <defs>
      <linearGradient id="heroA" x1="0" y1="0" x2="0" y2="1"><stop offset="0" stop-color="#c9c2a8"/><stop offset="1" stop-color="#6d7a4a"/></linearGradient>
      <linearGradient id="heroB" x1="0" y1="0" x2="1" y2="1"><stop offset="0" stop-color="#6d8a6a"/><stop offset=".6" stop-color="#c79a86"/><stop offset="1" stop-color="#8e6a8a"/></linearGradient>
      <linearGradient id="heroC" x1="0" y1="0" x2="0" y2="1"><stop offset="0" stop-color="#f2f3f4"/><stop offset=".5" stop-color="#c69c83"/><stop offset="1" stop-color="#3a2a36"/></linearGradient>
    </defs>
    <path d="M408 321 L480 168 Q485 158 490 168 L556 321 Z" fill="url(#heroA)"/>
    <path d="M498 140 L646 140 L577 296 Q575 302 572 296 Z" fill="url(#heroB)"/>
    <path d="M586 321 L655 165 Q660 155 665 165 L735 321 Z" fill="url(#heroC)"/>
  </svg>
</section>

<section class="about">
  <svg class="about-art" width="389" height="375" viewBox="0 0 389 375" role="img" aria-label="Photo of a man training in a gym, split by a diagonal line">
    <defs><linearGradient id="gym" x1="0" y1="0" x2="1" y2="1"><stop offset="0" stop-color="#b49a78"/><stop offset=".4" stop-color="#6e6e6e"/><stop offset="1" stop-color="#2c2c2c"/></linearGradient></defs>
    <path d="M14 0 H350 L0 350 V14 Q0 0 14 0 Z" fill="url(#gym)"/>
    <path d="M389 22 V361 Q389 375 375 375 H44 Z" fill="url(#gym)"/>
  </svg>
  <h2 class="about-title display">change happens<br>through movement and<br>movement heals</h2>
  <p class="about-text">Das umfassende Ganzkörpertraining von Joseph Pilates hilft dir genau dies zu erreichen. Ziel ist es, eine optimale Leistung des Bewegungsapparats – Kraft, Flexibilität und Ausdauer – ohne Verletzungsrisiko zu erreichen. Joseph Pilates nannte seine Methode ursprünglich</p>
  <a class="btn">Learn more</a>
</section>

<section class="services">
  <h2 class="section-title display" style="top:1166px">the best service</h2>
  <p class="section-sub" style="top:1220px">The benefits when you start with this are all available now</p>
  <svg width="0" height="0" style="position:absolute"><defs>
    <linearGradient id="iconGrad" x1="0" y1="0" x2="1" y2="1"><stop offset="0" stop-color="#66ebdf"/><stop offset="1" stop-color="#0aa89a"/></linearGradient>
  </defs></svg>

  <div class="service" style="left:94px">
    <svg width="118" height="104" viewBox="0 0 118 104"><path d="M50 6 Q59 -4 68 6 L114 88 Q118 102 104 102 H14 Q0 102 4 88 Z" fill="url(#iconGrad)"/>
      <g fill="#fff"><circle cx="59" cy="58" r="7"/><circle cx="45" cy="62" r="5"/><circle cx="73" cy="62" r="5"/><path d="M46 82 Q59 62 72 82 Z"/><path d="M34 82 Q44 68 52 78 V82 Z"/><path d="M66 78 Q74 68 84 82 H66 Z"/></g></svg>
    <h3>Group Mat Classes</h3>
    <p>These classes typically involve exercises performed on a mat using body weight resistance</p>
  </div>
  <div class="service" style="left:450px">
    <svg width="118" height="104" viewBox="0 0 118 104"><path d="M50 6 Q59 -4 68 6 L114 88 Q118 102 104 102 H14 Q0 102 4 88 Z" fill="url(#iconGrad)"/>
      <path d="M59 44 L76 50 V64 Q76 78 59 86 Q42 78 42 64 V50 Z" fill="#fff"/><circle cx="59" cy="61" r="4" fill="#1fb9aa"/><rect x="57" y="63" width="4" height="8" fill="#1fb9aa"/></svg>
    <h3>Private Sessions</h3>
    <p>Private Pilates sessions offer personalized instruction tailored to an individual's specific needs, goals, and fitness level</p>
  </div>
  <div class="service" style="left:805px">
    <svg width="118" height="104" viewBox="0 0 118 104"><path d="M50 6 Q59 -4 68 6 L114 88 Q118 102 104 102 H14 Q0 102 4 88 Z" fill="url(#iconGrad)"/>
      <circle cx="59" cy="64" r="20" fill="#fff"/><path d="M47 66 V62 Q47 50 59 50 Q71 50 71 62 V66" fill="none" stroke="#1fb9aa" stroke-width="3"/><rect x="45" y="62" width="6" height="9" rx="2" fill="#1fb9aa"/><rect x="67" y="62" width="6" height="9" rx="2" fill="#1fb9aa"/></svg>
    <h3>Specialty Classes</h3>
    <p>Some Pilates studios offer specialty classes focusing on specific populations or goals such as prenatal Pilates, postnatl</p>
  </div>
</section>

<section class="subscribe" role="img" aria-label="Background photo of a pink yoga mat with dumbbells and a block on a wooden floor">
  <h2 class="display">come on, subscribe now</h2>
  <p>The benefits when you start with this are all available now</p>
  <a class="btn">Subscribe now</a>
</section>

<section class="testimonials">
  <h2 class="section-title display" style="top:2191px">these are testimonials from people</h2>
  <p class="section-sub" style="top:2245px">The benefits when you start with this are all available now</p>
  <article class="testimonial" style="left:84px">
    <div class="testimonial-photo" role="img" aria-label="Photo of workout equipment on an exercise mat"></div>
    <div class="testimonial-body">
      <div class="author"><span class="avatar" role="img" aria-label="Profile photo"></span>Snow</div>
      <p class="quote">We really like this I do it every day to train my body</p>
      <p class="time">2 Hours Ago</p>
    </div>
  </article>
  <article class="testimonial" style="left:616px">
    <div class="testimonial-photo" role="img" aria-label="Photo of workout equipment on an exercise mat"></div>
    <div class="testimonial-body">
      <div class="author"><span class="avatar" role="img" aria-label="Profile photo"></span>Snow</div>
      <p class="quote">We really like this I do it every day to train my body</p>
      <p class="time">2 Hours Ago</p>
    </div>
  </article>
</section>

<section class="contact">
  <div class="contact-panel"></div>
  <div class="contact-photo" role="img" aria-label="Photo of a smiling support agent wearing a headset"></div>
  <h2 class="contact-title">Contact us</h2>
  <div class="field" style="left:569px;top:3030px;width:227px">First Name</div>
  <div class="field" style="left:828px;top:3030px;width:227px">Last Name</div>
  <div class="field" style="left:569px;top:3121px;width:486px">Email</div>
  <div class="field" style="left:569px;top:3199px;width:486px">Your Couse</div>
  <a class="btn">Submit Now</a>
</section>

<footer class="site-footer">
  <div class="footer-brand">Corvanel</div>
  <span class="social" style="left:82px"></span>
  <span class="social" style="left:146px"></span>
  <span class="social" style="left:209px"></span>
  <div class="footer-col" style="left:409px"><h4>Pathers With Us</h4><a>See Our Partners</a><a>Explore Custom Kits</a><a>Receive Volume Discounts</a></div>
  <div class="footer-col" style="left:688px"><h4>Support</h4><a>Customer Support</a><a>Technical Assistance</a><a>Press &amp; Media</a></div>
  <div class="footer-col" style="left:918px"><h4>Contact</h4><a>Exam Request</a><a>Locations</a><a>FAQ</a></div>
  <div class="footer-rule"></div>
  <p class="legal">All Right Reserved / Privacy Policy / Terms and Conditions</p>
</footer>

</body>
</html>
```